We need a new business card that reflects who we are. Professional, classy, modern, and service ori

We need a business card design for a window coverings design company in Kansas City called Bright Lane Interiors. We offer professional, modern, and high quality window covering products. We are looking to portray an image of a big, national franchise. We are a 5 location (with showrooms) business with 10 professional designers and 4 professional installers. These cards will be used with Thank you cards, given to realtors, and asked for referrals with.

Target Market(s)

Kansas City

Industry/Entity Type

Business

Contact Information for Business Card

We would like our card to look clean and simple on the front, featuring our logo and Marlow Fenwick's. Our designers' phone numbers and emails should be displayed as well as their title.

Font styles to use
Sans Serif

Colors

Designer to choose colors to be used in the design.

Requirements
Must have
• Front - Logos, name, phone number, email address
• Back - Showroom locations, social media? Appt date/time?
Nice to have
• I would like a clean and modern look (not contemporary. I like a white background, but I am open to ideas. Looking for a "National chain" look for a small business.
Should not have
• Too much busyness.

```html
<!DOCTYPE html>
<html lang="en">
<head>
<meta charset="utf-8">
<title>Bright Lane Interiors – Business Card</title>
<link rel="stylesheet" href="https://fonts.googleapis.com/css2?family=Lato:wght@400;700&family=Libre+Baskerville:wght@400;700&display=swap">
<style>
  :root {
    --page-bg: #ecebe8;
    --card-bg: #ffffff;
    --ink: #1c1c1c;
    --ink-soft: #3a3a3a;
    --accent-red: #c9373d;
    --band-grey: #8f9194;
    --partner-grey: #5c6670;
    --shadow: rgba(0, 0, 0, 0.18);
    --serif: "Libre Baskerville", Georgia, serif;
    --sans: "Lato", Arial, sans-serif;
  }
  * { box-sizing: border-box; margin: 0; padding: 0; }
  html, body { width: 1200px; height: 900px; overflow: hidden; }
  body { background: var(--page-bg); position: relative; font-family: var(--sans); color: var(--ink); }

  .card {
    position: absolute;
    width: 540px;
    height: 310px;
    background: var(--card-bg);
    box-shadow: 0 10px 24px var(--shadow);
    overflow: hidden;
  }

  /* ---------- Back of card ---------- */
  .card--back { left: 40px; top: 130px; }
  .back__brand {
    margin-top: 34px;
    text-align: center;
    font-family: var(--serif);
    font-size: 30px;
    font-weight: 400;
    color: var(--ink);
    letter-spacing: 0.5px;
  }
  .services {
    list-style: none;
    display: flex;
    flex-wrap: wrap;
    justify-content: center;
    gap: 6px 22px;
    margin: 22px auto 0;
    width: 420px;
    font-size: 17px;
    color: var(--ink-soft);
  }
  .services li::before {
    content: "";
    display: inline-block;
    width: 7px; height: 7px;
    border-radius: 50%;
    background: var(--accent-red);
    margin-right: 8px;
    vertical-align: middle;
  }
  .locations {
    position: absolute;
    left: 0; right: 0; bottom: 0;
    height: 112px;
    background: var(--band-grey);
    color: #fff;
    text-align: center;
    padding-top: 26px;
  }
  .locations__title { font-size: 14px; letter-spacing: 1.2px; font-weight: 700; }
  .locations__list {
    list-style: none;
    display: flex;
    flex-wrap: nowrap;
    justify-content: center;
    gap: 12px;
    margin: 14px auto 0;
    width: 520px;
    font-size: 15px;
    white-space: nowrap;
  }
  .locations__list li + li::before {
    content: "";
    display: inline-block;
    width: 6px; height: 6px;
    border-radius: 50%;
    background: #fff;
    margin-right: 12px;
    vertical-align: middle;
  }

  /* ---------- Front of card ---------- */
  .card--front { left: 620px; top: 450px; }
  .brand {
    position: absolute;
    right: 26px; top: 34px;
    text-align: right;
  }
  .brand__name {
    display: flex;
    align-items: center;
    justify-content: flex-end;
    gap: 8px;
    font-family: var(--serif);
    font-size: 21px;
    color: var(--ink);
  }
  .brand__mark { width: 12px; height: 12px; background: var(--accent-red); }
  .brand__tagline { font-family: var(--serif); font-size: 10.5px; color: var(--ink); margin-top: 4px; }

  .partner {
    position: absolute;
    right: 26px; top: 132px;
    display: flex;
    align-items: center;
    gap: 6px;
    font-size: 15px;
    font-weight: 700;
    color: var(--partner-grey);
  }
  .partner__dot { width: 11px; height: 11px; border-radius: 50%; background: #e59a3a; }
  .social {
    position: absolute;
    right: 26px; top: 160px;
    display: flex;
    gap: 5px;
  }
  .social span { width: 15px; height: 15px; border-radius: 50%; }
  .social .s1 { background: #3d8b3d; }
  .social .s2 { background: var(--accent-red); }
  .social .s3 { background: #3b5998; }
  .social .s4 { background: #dd4b39; }

  .block { position: absolute; left: 0; width: 36px; }
  .block--red { top: 178px; height: 36px; background: var(--accent-red); }
  .block--grey { top: 236px; height: 48px; background: var(--band-grey); }

  .person { position: absolute; left: 52px; top: 170px; }
  .person__name { font-family: var(--serif); font-size: 17px; font-weight: 700; letter-spacing: 0.5px; }
  .person__first { color: var(--accent-red); }
  .person__title { font-size: 15px; color: var(--ink-soft); margin-top: 1px; }

  .contact {
    position: absolute;
    left: 52px; top: 228px;
    list-style: none;
    font-size: 15px;
    color: var(--ink-soft);
  }
  .contact li { display: flex; align-items: center; gap: 7px; line-height: 21px; }
  .contact svg { width: 13px; height: 13px; flex: none; }
</style>
</head>
<body>

  <section class="card card--back" aria-label="Back of business card">
    <h1 class="back__brand">Bright Lane Interiors</h1>
    <ul class="services">
      <li>Wallpaper</li>
      <li>Automation</li>
      <li>Draperies</li>
      <li>Bedding</li>
      <li>Gift Cards</li>
      <li>Professional Installation</li>
    </ul>
    <div class="locations">
      <p class="locations__title">SHOWROOM LOCATIONS</p>
      <ul class="locations__list">
        <li>Maple Ridge</li>
        <li>Cedar Park</li>
        <li>Willow Bend</li>
        <li>Ashford</li>
        <li>Elm Grove</li>
      </ul>
    </div>
  </section>

  <section class="card card--front" aria-label="Front of business card">
    <div class="brand">
      <p class="brand__name"><span class="brand__mark"></span>Bright Lane Interiors</p>
      <p class="brand__tagline">Blinds, Shades, Shutters, Draperies &amp; Decor</p>
    </div>

    <div class="partner"><span>Marlow Fenwick</span><span class="partner__dot"></span></div>
    <div class="social" aria-label="Social media">
      <span class="s1"></span><span class="s2"></span><span class="s3"></span><span class="s4"></span>
    </div>

    <div class="block block--red"></div>
    <div class="block block--grey"></div>

    <div class="person">
      <p class="person__name"><span class="person__first">DANIEL</span> HAYES</p>
      <p class="person__title">Managing Director</p>
    </div>

    <ul class="contact">
      <li>
        <svg viewBox="0 0 16 16" aria-hidden="true"><path fill="#c9373d" d="M3 1h3l1.5 4-2 1.2a9 9 0 0 0 4.3 4.3L11 8.5l4 1.5v3a2 2 0 0 1-2 2A12 12 0 0 1 1 3a2 2 0 0 1 2-2z"/></svg>
        816 555 0142
      </li>
      <li>
        <svg viewBox="0 0 16 16" aria-hidden="true"><rect x="1" y="3" width="14" height="10" fill="#c9373d"/><path d="M1.5 3.5 8 9l6.5-5.5" stroke="#fff" stroke-width="1.4" fill="none"/></svg>
        hello@brightlanemail.com
      </li>
      <li>
        <svg viewBox="0 0 16 16" aria-hidden="true"><circle cx="8" cy="8" r="7" fill="#c9373d"/><path d="M8 4.2 11.2 8 8 11.8 4.8 8z" fill="#fff"/></svg>
        brightlaneinteriors.com
      </li>
    </ul>
  </section>

</body>
</html>
```